wealth management firm, professional group, new model

we have a logo that works but we need a card, white background using our colors...clean look

our tag line if can be used in

The Path From Saver To Investor

```html
<!DOCTYPE html>
<html lang="en">
<head>
<meta charset="utf-8">
<title>Velora Wealth Partners – Business Card</title>
<link href="https://fonts.googleapis.com/css2?family=Montserrat:wght@300;400;500;700&family=Josefin+Sans:wght@300;400&display=swap" rel="stylesheet">
<style>
  :root {
    --navy: #152a4c;
    --navy-deep: #10223f;
    --paper: #ffffff;
    --ink: #1d2f52;
    --muted: #5f6570;
    --rule: #b9bcc2;
    --stage: #e9eaec;
  }
  * { box-sizing: border-box; margin: 0; padding: 0; }
  html, body {
    width: 1200px; height: 900px; overflow: hidden;
    background: var(--stage);
    font-family: "Montserrat", sans-serif;
  }
  .sheet {
    width: 1200px; height: 900px;
    display: flex; flex-direction: column; align-items: center; justify-content: center;
    gap: 50px;
  }
  .card {
    width: 580px; height: 330px;
    border-radius: 30px;
    position: relative;
    box-shadow: 0 10px 26px rgba(20, 30, 50, 0.18);
    overflow: hidden;
  }

  /* Back side */
  .card--back {
    background: linear-gradient(160deg, var(--navy) 0%, var(--navy-deep) 100%);
    color: var(--paper);
  }
  .back-name {
    position: absolute; left: 0; right: 0; top: 118px;
    text-align: center;
    font-weight: 300; font-size: 26px; letter-spacing: 0.5em;
    padding-left: 0.5em;
  }
  .back-rule {
    position: absolute; left: 40px; right: 40px; top: 184px;
    height: 1px;
    background: linear-gradient(90deg, rgba(255,255,255,0) 0%, rgba(255,255,255,0.45) 50%, rgba(255,255,255,0) 100%);
  }
  .tagline {
    position: absolute; left: 0; right: 0; top: 204px;
    text-align: center;
    font-family: "Josefin Sans", sans-serif;
    font-weight: 400; font-size: 14px; letter-spacing: 0.42em;
    padding-left: 0.42em;
  }

  /* Front side */
  .card--front {
    background: linear-gradient(135deg, #f4f4f5 0%, var(--paper) 55%, #f2f2f3 100%);
    display: flex; align-items: center;
  }
  .brand {
    width: 300px;
    display: flex; flex-direction: column; align-items: center;
    color: var(--ink);
  }
  .brand__name {
    font-weight: 300; font-size: 38px; letter-spacing: 0.42em;
    padding-left: 0.42em;
  }
  .brand__sub {
    margin-top: 10px;
    font-weight: 400; font-size: 13px; letter-spacing: 0.2em;
  }
  .divider {
    width: 1px; height: 170px; background: var(--rule);
  }
  .contact {
    padding-left: 34px;
    color: var(--muted);
    font-size: 13px;
  }
  .contact__name {
    color: var(--ink); font-weight: 700; font-size: 17px; letter-spacing: 0.01em;
  }
  .contact__role { margin-top: 2px; margin-bottom: 16px; font-size: 13px; }
  .contact__row {
    display: flex; align-items: center; gap: 9px;
    margin-bottom: 7px;
  }
  .contact__row svg { width: 14px; height: 14px; flex: none; }
  .contact__row b { font-weight: 700; color: var(--muted); }
  .contact__address { margin-top: 10px; padding-left: 23px; line-height: 1.35; }
</style>
</head>
<body>
  <main class="sheet">
    <section class="card card--back" aria-label="Card back">
      <div class="back-name">VELORA</div>
      <div class="back-rule"></div>
      <p class="tagline">The Path From Saver To Investor</p>
    </section>

    <section class="card card--front" aria-label="Card front">
      <div class="brand">
        <div class="brand__name">VELORA</div>
        <div class="brand__sub">WEALTH PARTNERS</div>
      </div>
      <div class="divider"></div>
      <div class="contact">
        <div class="contact__name">JOHN SMITH</div>
        <div class="contact__role">Director</div>
        <div class="contact__row">
          <svg viewBox="0 0 24 24" fill="#1d2f52" aria-hidden="true"><path d="M6.6 10.8c1.4 2.8 3.8 5.1 6.6 6.6l2.2-2.2c.3-.3.7-.4 1-.2 1.1.4 2.3.6 3.6.6.6 0 1 .4 1 1V20c0 .6-.4 1-1 1C10.6 21 3 13.4 3 4c0-.6.4-1 1-1h3.5c.6 0 1 .4 1 1 0 1.3.2 2.5.6 3.6.1.3 0 .7-.2 1z"/></svg>
          <span>300-200-9000</span>
        </div>
        <div class="contact__row">
          <svg viewBox="0 0 24 24" fill="#1d2f52" aria-hidden="true"><path d="M2 5h20v14H2z"/><path d="M2 5l10 8 10-8" fill="none" stroke="#fff" stroke-width="1.6"/></svg>
          <span>info@<b>velorawealth</b>.com</span>
        </div>
        <div class="contact__row">
          <svg viewBox="0 0 24 24" fill="none" stroke="#1d2f52" stroke-width="1.8" aria-hidden="true"><circle cx="12" cy="12" r="9"/><path d="M3 12h18M12 3c3 3 3 15 0 18M12 3c-3 3-3 15 0 18"/></svg>
          <span>www.<b>velorawealth</b>.com</span>
        </div>
        <div class="contact__address">00 dummy city<br>dummy place 0000</div>
      </div>
    </section>
  </main>
</body>
</html>
```